Kelvaro Guest Event Collateral

Create a double-sided, oversized piece of collateral for a series of guest networking events that we'll be hosting in 2019

We are looking for this piece of collateral to be the size of an oversized post card (1/2 of an 8/5 x 11 piece of paper). The front should include the following: Kelvaro's Mission Statement: Continually foster a culture of community and education for focused business professionals. How do we do it? Using four distinct principles, Kelvaro offers business professionals the opportunity to be successful right now ,as well as next year. Through in-person meetings, virtual meetings, networking events, and educational opportunities Kelvaro offers members a chance to hit their goals not only this year, but every year! Collaboration: Work with like-minded, driven Kelvaro members to collaborate and overcome the objections, hurdles and challenges that all business professionals face, either in person at twice monthly meetings, or virtually, from the comfort of your home or office. Accountability: Stay on track, and complete the goals you have set for yourself! Weekly in person or virtual meetings afford all members the opportunity to review their plan twice a month with fellow Kelvaro members, and trained Kelvaro coaches. Referrals: In the midst of crafting an executable, measurable and attainable plan let Kelvaro build your business through a steady stream of referrals via six yearly networking events, specifically designed to ensure you walk away with new referral partners. Strategy: Let Kelvaro assist you in crafting a strategy within our proven business planning template; realistic, understandable, measurable, beyond normal, attainable and time bound. The back should include the following: Become a Kelvaro member for $150/month and join us for 6 Networking Events in 2019 plus much more! We aren’t just about collaboration, accountability and strategy! Creating opportunities for referrals is also a cornerstone of Kelvaro! To make certain we are delivering on this principle, Kelvaro will host 6 events throughout 2019, complete with specific activities at each event to ensure you meet everyone in the room, making immediate connects to build your referral network. Join now and put yourself in position for success in 2019! Name: Phone: Email: Company Name: Industry: Position: Credit Card Number: Exp. Date: Testimonials: Overall I think people are lazy. I know I am! The benefits I have found and have come to truly appreciate thru Kelvaro are a sense of professionalism, accountability and shared enthusiasm. These things break that cycle of laziness for me and, I am sure, many others. When I walk into a meeting I know that positive and helpful feedback is the name of the game. Feedback from others and in many other industries from my own has become a key and cornerstone to my business and personal success. I would urge anyone no matter what your occupation to attend a couple of meetings and see how this group of like minded professionals can help you to achieve more. More time, More success, More health, More security, More money, More happiness..............What could you use more of? Gordon T. Mabry Sr. Automotive Consultant Bramblewick Leasing & Sales Thank you!

Target Market(s)

Small business owners, entrpreneurs, networkers, sales people

Industry/Entity Type

Business Consultant

Font styles to use
Sans Serif

Colors
f36f22
f68d4e
f8ba93
f78f20
faa54b

Requirements
Must have
• - Imagery
• - Our company logo
• - Clear CTA to check out our website (www.kelvaro-example.com)
• - Option to "Join the Kelvaro Community Today!" and include a spot for someone to fill in their name, email address, company name, and phone number
• - Reference that we host 6+ networking events in Denver throughout the year that are free to attend and are unlike any other networking event they've attended before
• - Mention that we have in-person meetings 2x per month, virtual meeting options, networking events, and educational events
• - Highlight the following acronym which references our core company components:
• Collaboration:
• Work with like-minded, driven Kelvaro members to collaborate and overcome the objections, hurdles and challenges that all business professionals face, in either in person twice monthly meetings, or virtually, from the comfort of your home of office.
• Accountability:
• Stay on track, and complete the goals you have set for yourself! Weekly in person or virtual meetings afford all members the opportunity to review their plan twice a month with your fellow Kelvaro members and trained Kelvaro coaches, to make certain you success is continuous throughout the year.
• Referrals:
• In the midst of crafting an executable, measurable and attainable plan let Kelvaro build your business through a steady stream of referral opportunities via twelve yearly networking events, specifically designed to ensure you walk away with new referral partners.
• Strategy:
• Let Kelvaro assist you in crafting a strategy within our proven business planning template; realistic, understandable, measurable, beyond normal, attainable and time bound.

```html
<!DOCTYPE html>
<html lang="en">
<head>
<meta charset="utf-8">
<title>Kelvaro Guest Event Collateral</title>
<link href="https://fonts.googleapis.com/css2?family=Lato:wght@300;400;700&display=swap" rel="stylesheet">
<style>
  :root{
    --orange:#f68d2e;
    --orange-deep:#f36f22;
    --orange-soft:#faa54b;
    --orange-pale:#f8ba93;
    --charcoal:#4e4e50;
    --grey:#8d8e90;
    --grey-light:#e4e4e4;
    --ink:#3c3c3c;
    --paper:#ffffff;
    --backdrop:#ededed;
  }
  *{box-sizing:border-box;margin:0;padding:0}
  html,body{width:1200px;height:770px;overflow:hidden}
  body{background:var(--backdrop);font-family:"Lato",sans-serif;color:var(--ink);position:relative}
  .flyer{position:absolute;top:45px;width:525px;height:680px;background:var(--paper);overflow:hidden;box-shadow:0 2px 8px rgba(0,0,0,.18)}
  .flyer--front{left:50px}
  .flyer--back{left:625px}
  .flyer__art{position:absolute;inset:0;width:525px;height:680px;z-index:2}
  .brand{position:absolute;left:25px;top:18px;display:flex;align-items:center;gap:9px;z-index:3}
  .brand__mark{width:30px;height:30px;background:var(--orange)}
  .brand__name{font-weight:400;font-size:36px;letter-spacing:.5px;color:#58595b;line-height:1}
  .photo{position:absolute;left:0;top:70px;width:525px;height:230px;z-index:1}
  .photo--meeting{background:linear-gradient(120deg,#d9dde0 0%,#a9b4bc 30%,#c8b39c 55%,#5d6f7e 80%,#2f3e4d 100%)}
  .photo--planning{background:linear-gradient(110deg,#b9a48c 0%,#e8e4dc 35%,#f2f1ee 60%,#c9c2b6 85%,#8d7a66 100%)}
  .title-band{position:absolute;left:0;top:283px;height:41px;background:var(--orange);color:#fff;font-weight:400;font-size:21px;line-height:41px;padding-left:26px;z-index:3;clip-path:polygon(0 0,calc(100% - 10px) 0,100% 100%,0 100%)}
  .flyer--front .title-band{width:388px}
  .flyer--back .title-band{width:387px}
  .lede{position:absolute;left:26px;top:336px;width:480px;font-size:11.2px;line-height:19px;color:var(--ink);z-index:3}
  .signup{position:absolute;left:26px;top:378px;width:476px;border:1.5px solid var(--orange-soft);border-radius:7px;overflow:hidden;z-index:3;background:#fff}
  .signup__row{display:flex;height:22.5px;border-bottom:2px solid #fff}
  .signup__row:last-child{border-bottom:none}
  .signup__label{width:104px;background:var(--orange);color:#fff;font-size:9px;line-height:22.5px;padding-left:9px}
  .signup__field{flex:1;background:var(--grey-light);margin-left:2px}
  .offers{position:absolute;left:26px;top:490px;width:470px;display:grid;grid-template-columns:258px 1fr;row-gap:10px;z-index:3}
  .offer{display:flex;align-items:center;gap:12px;font-size:13px;color:var(--ink)}
  .offer__icon{width:36px;height:36px;flex:none}
  .components{position:absolute;left:26px;top:343px;width:476px;display:grid;grid-template-columns:232px 232px;column-gap:12px;row-gap:10px;z-index:3}
  .component__head{display:flex;align-items:center;gap:8px;color:var(--orange);font-weight:700;font-size:13px;letter-spacing:.2px;margin-bottom:4px;height:22px}
  .component__head svg{width:24px;height:22px;flex:none}
  .component__text{font-size:9.6px;line-height:12.2px;text-align:justify;hyphens:auto;color:var(--ink)}
  .contact{position:absolute;left:26px;top:609px;z-index:3;list-style:none}
  .contact li{display:flex;align-items:center;gap:8px;color:#fff;font-size:11.5px;height:19.5px}
  .contact svg{width:14px;height:14px;flex:none}
</style>
</head>
<body>

<svg width="0" height="0" style="position:absolute" aria-hidden="true">
  <defs>
    <radialGradient id="badge" cx="40%" cy="35%" r="70%">
      <stop offset="0" stop-color="#faa54b"/>
      <stop offset="1" stop-color="#f36f22"/>
    </radialGradient>
    <g id="top-sweep">
      <path d="M300 0 L525 0 L525 105 C480 60 410 22 300 0 Z" fill="#f68d2e"/>
      <path d="M360 70 C440 88 495 120 525 150 L525 70 Z" fill="#fff"/>
      <path d="M318 6 C420 28 490 70 525 118" fill="none" stroke="#8d8e90" stroke-width="6"/>
      <path d="M340 16 C430 40 495 82 525 132" fill="none" stroke="#c9c9ca" stroke-width="3"/>
    </g>
    <g id="foot-sweep">
      <path d="M0 574 L525 662 L525 680 L0 680 Z" fill="#4e4e50"/>
      <path d="M290 680 C400 660 475 618 525 578 L525 680 Z" fill="#fff"/>
      <path d="M350 680 C430 665 490 638 525 614 L525 680 Z" fill="#f68d2e"/>
      <path d="M270 682 C390 655 475 607 525 556" fill="none" stroke="#8d8e90" stroke-width="7"/>
    </g>
  </defs>
</svg>

<section class="flyer flyer--front">
  <div class="brand"><span class="brand__mark"></span><span class="brand__name">KELVARO</span></div>
  <div class="photo photo--meeting" role="img" aria-label="Photo of professionals smiling and talking around a meeting table with laptops"></div>
  <svg class="flyer__art" viewBox="0 0 525 680" aria-hidden="true">
    <use href="#top-sweep"/><use href="#foot-sweep"/>
  </svg>
  <h1 class="title-band">Join the Kelvaro Community Today!</h1>
  <p class="lede">We host 6+ networking events in Denver throughout the year<br>that are free to attend and are unlike any other networking event they've attended before</p>
  <form class="signup">
    <div class="signup__row"><label class="signup__label">Your name:</label><span class="signup__field"></span></div>
    <div class="signup__row"><label class="signup__label">Phone number:</label><span class="signup__field"></span></div>
    <div class="signup__row"><label class="signup__label">Email address:</label><span class="signup__field"></span></div>
    <div class="signup__row"><label class="signup__label">Company name:</label><span class="signup__field"></span></div>
  </form>
  <div class="offers">
    <div class="offer">
      <svg class="offer__icon" viewBox="0 0 36 36"><circle cx="18" cy="18" r="17" fill="url(#badge)"/><rect x="10" y="11" width="16" height="15" rx="1.5" fill="none" stroke="#fff" stroke-width="1.6"/><line x1="10" y1="15" x2="26" y2="15" stroke="#fff" stroke-width="1.6"/><g fill="#fff"><rect x="12.5" y="17.5" width="3" height="2.5"/><rect x="16.5" y="17.5" width="3" height="2.5"/><rect x="20.5" y="17.5" width="3" height="2.5"/><rect x="12.5" y="21" width="3" height="2.5"/><rect x="16.5" y="21" width="3" height="2.5"/></g></svg>
      <span>In-person meetings 2x per month</span>
    </div>
    <div class="offer">
      <svg class="offer__icon" viewBox="0 0 36 36"><circle cx="18" cy="18" r="17" fill="url(#badge)"/><g fill="#fff"><circle cx="18" cy="13" r="3.2"/><path d="M12 24c0-4 2.7-6 6-6s6 2 6 6z"/><circle cx="11" cy="15" r="2.4"/><path d="M6.5 23c0-3 2-4.5 4.5-4.5 1 0 1.8.2 2.4.6-.8 1-1.3 2.4-1.4 3.9z"/><circle cx="25" cy="15" r="2.4"/><path d="M29.5 23c0-3-2-4.5-4.5-4.5-1 0-1.8.2-2.4.6.8 1 1.3 2.4 1.4 3.9z"/></g></svg>
      <span>Networking events</span>
    </div>
    <div class="offer">
      <svg class="offer__icon" viewBox="0 0 36 36"><circle cx="18" cy="18" r="17" fill="url(#badge)"/><g fill="#fff"><circle cx="18" cy="13" r="4"/><path d="M10 27c0-5 3.5-8 8-8s8 3 8 8z"/></g></svg>
      <span>Virtual meeting options</span>
    </div>
    <div class="offer">
      <svg class="offer__icon" viewBox="0 0 36 36"><circle cx="18" cy="18" r="17" fill="url(#badge)"/><circle cx="15" cy="20" r="5.5" fill="none" stroke="#fff" stroke-width="3" stroke-dasharray="3 2"/><circle cx="15" cy="20" r="2" fill="#fff"/><circle cx="23" cy="12" r="3.5" fill="none" stroke="#fff" stroke-width="2" stroke-dasharray="2 1.5"/></svg>
      <span>Educational events</span>
    </div>
  </div>
  <ul class="contact">
    <li><svg viewBox="0 0 14 14"><circle cx="7" cy="7" r="7" fill="#f68d2e"/><path d="M5 4l1.3 1.8-.8.8c.5 1 1.2 1.7 2.2 2.2l.8-.8L10 9.3 9.1 10.4C6.5 10 4 7.5 3.7 5z" fill="#fff"/></svg>00000000000</li>
    <li><svg viewBox="0 0 14 14"><circle cx="7" cy="7" r="7" fill="#f68d2e"/><rect x="3.5" y="4.5" width="7" height="5" fill="#fff"/><path d="M3.5 4.5L7 7.3l3.5-2.8" fill="none" stroke="#f68d2e" stroke-width=".9"/></svg>hello@kelvaro-example.com</li>
    <li><svg viewBox="0 0 14 14"><circle cx="7" cy="7" r="7" fill="#f68d2e"/><g fill="none" stroke="#fff" stroke-width=".9"><circle cx="7" cy="7" r="3.8"/><ellipse cx="7" cy="7" rx="1.6" ry="3.8"/><line x1="3.2" y1="7" x2="10.8" y2="7"/></g></svg>www.kelvaro-example.com</li>
  </ul>
</section>

<section class="flyer flyer--back">
  <div class="brand"><span class="brand__mark"></span><span class="brand__name">KELVARO</span></div>
  <div class="photo photo--planning" role="img" aria-label="Photo of hands reviewing printed business charts and planning documents on a desk"></div>
  <svg class="flyer__art" viewBox="0 0 525 680" aria-hidden="true">
    <use href="#top-sweep"/><use href="#foot-sweep"/>
  </svg>
  <h2 class="title-band">Our core company components:</h2>
  <div class="components">
    <article class="component">
      <h3 class="component__head"><svg viewBox="0 0 24 22"><g fill="#4e4e50"><circle cx="9" cy="6" r="4"/><path d="M1 19c0-5 3.5-7.5 8-7.5s8 2.5 8 7.5z"/><path d="M18 7l4 4M22 7l-4 4" stroke="#4e4e50" stroke-width="1.8"/></g></svg>COLLABORATION</h3>
      <p class="component__text">Work with like-minded, driven Kelvaro members to collaborate and overcome the objections, hurdles and challenges that all business professionals face, in either in person twice monthly meetings, or virtually, from the comfort of your home or office.</p>
    </article>
    <article class="component">
      <h3 class="component__head"><svg viewBox="0 0 24 22"><g fill="#4e4e50"><rect x="1" y="16" width="3" height="4"/><rect x="6" y="13" width="3" height="7"/><rect x="11" y="9" width="3" height="11"/><rect x="16" y="5" width="3" height="15"/><rect x="21" y="1" width="3" height="19"/></g></svg>REFERRALS</h3>
      <p class="component__text">In the midst of crafting an executable, measurable and attainable plan let Kelvaro build your business through a steady stream of referral opportunities via twelve yearly networking events, specifically designed to ensure you walk away with new referral partners.</p>
    </article>
    <article class="component">
      <h3 class="component__head"><svg viewBox="0 0 24 22"><g fill="#4e4e50"><rect x="10" y="2" width="12" height="17" rx="1"/><circle cx="8" cy="13" r="5" fill="none" stroke="#4e4e50" stroke-width="2"/><line x1="4.5" y1="16.5" x2="1" y2="20.5" stroke="#4e4e50" stroke-width="2.4"/></g></svg>ACCOUNTABILITY</h3>
      <p class="component__text">Stay on track, and complete the goals you have set for yourself! Weekly in person or virtual meetings afford all members the opportunity to review their plan twice a month with your fellow Kelvaro members and trained Kelvaro coaches, to make certain your success is continuous throughout the year.</p>
    </article>
    <article class="component">
      <h3 class="component__head"><svg viewBox="0 0 24 22"><g fill="#4e4e50"><path d="M12 3L1 8l11 5 11-5z"/><path d="M5 11v5c2 2 12 2 14 0v-5l-7 3z"/><rect x="21" y="8" width="1.3" height="7"/></g></svg>STRATEGY</h3>
      <p class="component__text">Let Kelvaro assist you in crafting a strategy within our proven business planning template; realistic, understandable, measurable, beyond normal, attainable and time bound.</p>
    </article>
  </div>
  <ul class="contact">
    <li><svg viewBox="0 0 14 14"><circle cx="7" cy="7" r="7" fill="#f68d2e"/><path d="M5 4l1.3 1.8-.8.8c.5 1 1.2 1.7 2.2 2.2l.8-.8L10 9.3 9.1 10.4C6.5 10 4 7.5 3.7 5z" fill="#fff"/></svg>00000000000</li>
    <li><svg viewBox="0 0 14 14"><circle cx="7" cy="7" r="7" fill="#f68d2e"/><rect x="3.5" y="4.5" width="7" height="5" fill="#fff"/><path d="M3.5 4.5L7 7.3l3.5-2.8" fill="none" stroke="#f68d2e" stroke-width=".9"/></svg>hello@kelvaro-example.com</li>
    <li><svg viewBox="0 0 14 14"><circle cx="7" cy="7" r="7" fill="#f68d2e"/><g fill="none" stroke="#fff" stroke-width=".9"><circle cx="7" cy="7" r="3.8"/><ellipse cx="7" cy="7" rx="1.6" ry="3.8"/><line x1="3.2" y1="7" x2="10.8" y2="7"/></g></svg>www.kelvaro-example.com</li>
  </ul>
</section>

</body>
</html>
```